MD Trailcraft & Wildland Fair

I need a 1 page flyer for promotion of an upcoming sportsman and outdoor show(expo). would like the flyer to be able to be printed in B&W and color! show will include all things to do with the out doors, hunting fishing boating hiking atv camping rvs motorcycles. the event will have a kids zone, events games and activities for kids. there will be vendors showing the newest products. guest speakers and industry experts giving training and advice. this show will have something for everyone. food trucks and concessions. 200+ vendors. waterfould calling competition. deer/buck scoring casting competition for kids 3D Archery competitions

Target Market(s)

anyone event open to all ages!

Colors
ec1f27
000000
fbed22

Requirements
Must have
• date- september 1-2 2018
• location Pelling valley expo 4837 orchardmill rd east calverton MD 21652
• facebook - mdtrailcraftfair
• email mdtrailcraftfair@quorvex.com
• web www.mdtrailcraftfair.com
• vendor spaces still available! sign up now space going fast
Nice to have
• would like some thing that can be both printed in B&W and Color, and still have a great affect.
Should not have
• open to any suggestions

```html
<!DOCTYPE html>
<html lang="en">
<head>
<meta charset="utf-8">
<title>MD Trailcraft &amp; Wildland Fair</title>
<link href="https://fonts.googleapis.com/css2?family=Cinzel:wght@400;700&family=Kalam:wght@400&family=Dancing+Script:wght@400&display=swap" rel="stylesheet">
<style>
  :root{
    --page:#ffffff;
    --board:#6f6763;
    --board-dark:#5c5551;
    --plank-line:#4a4340;
    --paper:#dcd4d1;
    --paper-shade:#c9c0bd;
    --band:#8e8483;
    --ink:#1b1616;
    --ink-soft:#4a4242;
    --ink-faint:#8f8786;
    --polaroid:#ffffff;
    --pin:#8a807e;
    --title-text:#d9cfc9;
  }
  *{box-sizing:border-box;margin:0;padding:0}
  html,body{width:1200px;height:1200px;overflow:hidden;background:var(--page)}
  .flyer{position:relative;width:1200px;height:1200px}
  .board{position:absolute;left:54px;top:214px;width:1092px;height:772px;
    background:linear-gradient(100deg,var(--board) 0%,var(--board-dark) 50%,var(--board) 100%);overflow:hidden}
  .board svg{position:absolute;inset:0}
  .pin{position:absolute;width:14px;height:14px;border-radius:50%;
    background:radial-gradient(circle at 35% 35%,#bdb4b2,var(--pin) 60%,#5d5553);
    box-shadow:1px 2px 3px rgba(0,0,0,.45);z-index:5}
  .polaroid{position:absolute;background:var(--polaroid);padding:14px 14px 40px;
    box-shadow:3px 5px 10px rgba(0,0,0,.45)}
  .polaroid .photo{width:100%;height:100%}
  .photo--fishing{background:linear-gradient(180deg,#6d6765 0%,#a8a2a0 45%,#5b5654 100%)}
  .photo--jetski{background:linear-gradient(180deg,#4f4a49 0%,#8c8684 55%,#b8b2b0 100%)}
  .photo--moto{background:linear-gradient(160deg,#a19b99 0%,#6e6866 60%,#8b8583 100%)}
  .photo--hiker{background:linear-gradient(180deg,#4a4544 0%,#8a8482 55%,#5e5957 100%)}

  .notice{position:absolute;left:346px;top:226px;width:606px;height:372px;
    background:linear-gradient(135deg,var(--paper),var(--paper-shade));
    transform:rotate(0.6deg);box-shadow:3px 5px 10px rgba(0,0,0,.4);text-align:center;color:var(--ink)}
  .notice__title{position:absolute;left:84px;top:28px;width:436px;height:92px;background:var(--ink);
    font-family:'Cinzel',serif;font-weight:700;color:var(--title-text);font-size:33px;line-height:40px;padding-top:6px}
  .notice__star{position:absolute;top:22px;font-family:'Cinzel',serif;font-size:40px;color:var(--ink)}
  .notice__date{position:absolute;left:0;right:0;top:130px;font-family:'Cinzel',serif;font-weight:700;font-size:21px;letter-spacing:1px}
  .notice__rule{position:absolute;left:150px;width:306px;top:162px;height:3px;background:var(--ink-faint)}
  .notice__venue{position:absolute;left:0;right:0;top:172px;font-family:'Cinzel',serif;font-size:11.5px;line-height:14px}
  .notice__banner{position:absolute;left:38px;top:218px;width:530px;height:56px}
  .notice__banner svg{position:absolute;inset:0}
  .notice__banner p{position:relative;font-family:'Cinzel',serif;font-weight:700;color:var(--title-text);font-size:15.5px;line-height:20px;padding-top:8px;letter-spacing:.5px}
  .notice__list{position:absolute;left:16px;right:16px;top:282px;font-family:'Kalam',cursive;font-size:12.5px;line-height:16.5px;color:var(--ink)}

  .social{position:absolute;left:364px;top:578px;width:578px;height:114px;background:var(--band);
    box-shadow:2px 4px 8px rgba(0,0,0,.35);display:flex;align-items:center;justify-content:center;gap:24px;
    font-family:'Cinzel',serif;font-weight:700;font-size:18px;color:var(--ink);letter-spacing:1px}
  .social__mark{width:60px;height:60px;background:var(--ink);border-radius:8px}

  .contact{position:absolute;left:56px;top:508px;width:312px;height:196px;
    background:linear-gradient(135deg,var(--paper),var(--paper-shade));transform:rotate(2deg);
    box-shadow:3px 5px 10px rgba(0,0,0,.4);text-align:center;padding-top:48px;font-family:'Kalam',cursive;color:var(--ink)}
  .contact__head{font-family:'Cinzel',serif;font-weight:700;font-size:19px;color:var(--ink-faint);letter-spacing:1px;margin-bottom:4px}
  .contact__line{font-size:17px;line-height:24px}

  .pitch{position:absolute;left:446px;top:654px;width:420px;height:312px;
    background:linear-gradient(135deg,var(--paper),var(--paper-shade));transform:rotate(-4deg);
    box-shadow:3px 5px 10px rgba(0,0,0,.4);text-align:center;color:var(--ink)}
  .pitch__text{padding-top:30px;font-family:'Cinzel',serif;font-weight:700;font-size:16px;line-height:21px;letter-spacing:.5px}
  .pitch__script{position:absolute;left:20px;top:200px;width:380px;font-family:'Dancing Script',cursive;
    font-size:27px;line-height:32px;color:var(--ink-faint);transform:rotate(-14deg)}
</style>
</head>
<body>
<main class="flyer">
  <div class="board">
    <svg width="1092" height="772" aria-hidden="true">
      <g stroke="var(--plank-line)" stroke-width="2" opacity=".6">
        <line x1="118" y1="0" x2="118" y2="772"/><line x1="262" y1="0" x2="262" y2="772"/>
        <line x1="404" y1="0" x2="404" y2="772"/><line x1="548" y1="0" x2="548" y2="772"/>
        <line x1="694" y1="0" x2="694" y2="772"/><line x1="838" y1="0" x2="838" y2="772"/>
        <line x1="982" y1="0" x2="982" y2="772"/>
      </g>
    </svg>
  </div>

  <!-- photo board -->
  <figure class="polaroid" style="left:82px;top:254px;width:252px;height:240px;transform:rotate(-5deg)">
    <div class="photo photo--fishing" role="img" aria-label="Angler in silhouette fishing from a pier at dusk"></div>
  </figure>
  <span class="pin" style="left:206px;top:246px"></span>

  <figure class="polaroid" style="left:920px;top:272px;width:220px;height:264px;transform:rotate(-1deg)">
    <div class="photo photo--jetski" role="img" aria-label="Rider on a jet ski spraying through the water"></div>
  </figure>
  <span class="pin" style="left:1032px;top:270px"></span>

  <figure class="polaroid" style="left:108px;top:716px;width:232px;height:266px">
    <div class="photo photo--moto" role="img" aria-label="Motocross rider kicking up dust on a dirt bike"></div>
  </figure>
  <span class="pin" style="left:210px;top:720px"></span>

  <figure class="polaroid" style="left:892px;top:668px;width:236px;height:262px;transform:rotate(-2deg)">
    <div class="photo photo--hiker" role="img" aria-label="Hiker with a backpack and pole looking over mountains"></div>
  </figure>
  <span class="pin" style="left:984px;top:664px"></span>

  <!-- main notice -->
  <section class="notice">
    <span class="notice__star" style="left:56px">*</span>
    <h1 class="notice__title">MD TRAILCRAFT &amp;<br>WILDLAND FAIR</h1>
    <span class="notice__star" style="right:56px">*</span>
    <p class="notice__date">SEPTEMBER 1-2, 2018</p>
    <div class="notice__rule"></div>
    <p class="notice__venue">PELLING VALLEY EXPO<br>4837 ORCHARDMILL RD<br>EAST CALVERTON MD 21652</p>
    <div class="notice__banner">
      <svg width="530" height="56" aria-hidden="true">
        <polygon points="10,0 520,0 530,10 530,46 520,56 10,56 0,46 0,10" fill="var(--ink)"/>
        <polygon points="16,5 514,5 524,14 524,42 514,51 16,51 6,42 6,14" fill="var(--band)"/>
        <polygon points="20,8 510,8 520,16 520,40 510,48 20,48 10,40 10,16" fill="#5b5353"/>
      </svg>
      <p>OVER 60,000 SQFT OF INDOOR AND 30,000+ SQFT<br>OUTDOOR PRODUCTS AND SERVICES INCLUDING:</p>
    </div>
    <p class="notice__list">*Sports Equipment *Campers *Boats *RV's *Tackle &amp; Bait *Motorcycles *ATV's *Trucks *Taxidermists *Outfitters *Guns *Jet Skis *Charter Boats *Golf Resorts *Knives *Archery *Trailers *Sporting Clubs *Game Calls * Outdoor Magazines *Camp Grounds *Camping Equipment * Hunting Supplies * and much more...</p>
  </section>
  <span class="pin" style="left:372px;top:234px"></span>
  <span class="pin" style="left:912px;top:238px"></span>

  <div class="social">
    <span>FOLLOW US ON</span>
    <span class="social__mark" aria-hidden="true"></span>
    <span>MDTRAILCRAFTFAIR</span>
  </div>

  <!-- contact card -->
  <section class="contact">
    <h2 class="contact__head">CONTACT US TODAY</h2>
    <p class="contact__line">mdtrailcraftfair@quorvex.com</p>
    <p class="contact__line">www.mdtrailcraftfair.com</p>
    <p class="contact__line">DANA 410-555-0187</p>
  </section>
  <span class="pin" style="left:190px;top:516px"></span>

  <!-- vendor pitch -->
  <section class="pitch">
    <p class="pitch__text">SELL YOUR PRODUCTS AND SERVICES<br>TO THOUSANDS OF PEOPLE<br>IN ONE WEEKEND!!<br>WE ARE EXPECTING 2 DAY<br>ATTENDANCE TO TOP 15,000<br>PEOPLE!</p>
    <p class="pitch__script">Vendor spaces still available!<br>sign up now space going fast</p>
  </section>
  <span class="pin" style="left:782px;top:652px"></span>
</main>
</body>
</html>
```